'CALVENTO' NEW WINE LABEL DESIGN

I am looking for an exceptional and exciting design for a wine label called 'Calvento' meaning 'Lookout'. The design must feature the name 'Calvento', and the word 'Cabernet Sauvignon' in version 1 and 'Sauvignon Blanc' in version 2. It will also need the words 'Valle Central, Chile' at the bottom of the label as a prominent piece of information as well as the vintage 2017. Please produce the work in size 80mm x 100mm. Feel free to use colour in addition to black/white and ensue that the label is easy to read on a shelf placement.
Target Market(s)
SUPERMARKETS & WINE STORES
Requirements
Must have
- EASY TO READ, USE COLOURS LIKE GREEN FOR SAUVIGNON & RED FOR CABERNET SAUVIGNON
- FULL BOTTLE SHOT MUST BE IN PROVIDED DESIGNS. ALL BOTTLE TOPS SHOULD BE QUORLEX STYLE (SCREW TOP)
- PLEASE NOTE THAT LABEL INFORMATION MUSY BE EASY TO READ I.E. VINTAGE, PLACE OF ORGIN ALTHOUGH NOT THE MAIN CONTENT MUST STILL BE CLEAR.
Nice to have
- ARTISTIC REFERENCE LINK TO NAME & ANDES BUT NOT PICTURES OF MOUNTAINS
Should not have
- PICTURES OF GRAPES
- PICTURES OF VINEYARDS
- PICTURES OF MOUNTAINS

```html
<!DOCTYPE html>
<html lang="en">
<head>
<meta charset="utf-8">
<title>Calvento wine labels</title>
<link href="https://fonts.googleapis.com/css2?family=Cormorant+Garamond:wght@500;600&family=Questrial&display=swap" rel="stylesheet">
<style>
  :root {
    --page: #ffffff;
    --label-paper: #f3efd9;
    --ink: #2a2623;
    --ink-soft: #8d8a80;
    --band-blanc: #f6d4a4;
    --band-cabernet: #b3303f;
    --peak-light: #eef1f0;
    --peak-shade: #b7c6cc;
  }
  * { margin: 0; padding: 0; box-sizing: border-box; }
  html, body {
    width: 934px;
    height: 1200px;
    overflow: hidden;
    background: var(--page);
  }
  .label-set {
    position: relative;
    width: 934px;
    height: 1200px;
    display: flex;
    justify-content: center;
    align-items: center;
    gap: 54px;
  }
  .wine-label {
    position: relative;
    width: 400px;
    height: 490px;
    background: var(--label-paper);
    box-shadow: 0 1px 4px rgba(0,0,0,0.12);
    overflow: hidden;
  }
  .colour-band {
    position: absolute;
    left: 0; top: 0;
    width: 100%;
    height: 90px;
  }
  .wine-label--blanc .colour-band { background: var(--band-blanc); }
  .wine-label--cabernet .colour-band { background: var(--band-cabernet); }
  .peak-artwork {
    position: absolute;
    left: 0; top: 24px;
    width: 100%;
    height: 140px;
    display: block;
  }
  .brand-name {
    position: absolute;
    top: 262px;
    width: 100%;
    text-align: center;
    font-family: "Cormorant Garamond", serif;
    font-weight: 500;
    font-size: 40px;
    letter-spacing: 0.24em;
    padding-left: 0.24em;
    color: var(--ink);
  }
  .varietal {
    position: absolute;
    top: 328px;
    width: 100%;
    text-align: center;
    font-family: "Cormorant Garamond", serif;
    font-weight: 600;
    font-size: 13px;
    letter-spacing: 0.08em;
    color: var(--ink);
  }
  .vintage {
    position: absolute;
    top: 406px;
    width: 100%;
    text-align: center;
    font-family: "Questrial", sans-serif;
    font-size: 20px;
    letter-spacing: 0.14em;
    padding-left: 0.14em;
    color: var(--ink);
  }
  .origin {
    position: absolute;
    top: 462px;
    width: 100%;
    text-align: center;
    font-family: "Cormorant Garamond", serif;
    font-weight: 600;
    font-size: 11px;
    letter-spacing: 0.3em;
    padding-left: 0.3em;
    color: var(--ink-soft);
  }
</style>
</head>
<body>
  <main class="label-set">
    <article class="wine-label wine-label--blanc">
      <div class="colour-band"></div>
      <svg class="peak-artwork" viewBox="0 0 400 140" preserveAspectRatio="none" role="img" aria-label="Engraved illustration of a snowy Andean peak">
        <defs>
          <linearGradient id="peakFillBlanc" x1="0" y1="0" x2="0" y2="1">
            <stop offset="0" stop-color="var(--peak-light)"/>
            <stop offset="0.6" stop-color="var(--peak-shade)"/>
            <stop offset="1" stop-color="var(--label-paper)"/>
          </linearGradient>
        </defs>
        <rect x="0" y="0" width="400" height="140" fill="url(#peakFillBlanc)"/>
      </svg>
      <h1 class="brand-name">CALVENTO</h1>
      <p class="varietal">SAUVIGNON BLANC</p>
      <p class="vintage">2017</p>
      <p class="origin">VALLE CENTRAL, CHILE</p>
    </article>

    <article class="wine-label wine-label--cabernet">
      <div class="colour-band"></div>
      <svg class="peak-artwork" viewBox="0 0 400 140" preserveAspectRatio="none" role="img" aria-label="Engraved illustration of a snowy Andean peak">
        <defs>
          <linearGradient id="peakFillCabernet" x1="0" y1="0" x2="0" y2="1">
            <stop offset="0" stop-color="var(--peak-light)"/>
            <stop offset="0.6" stop-color="var(--peak-shade)"/>
            <stop offset="1" stop-color="var(--label-paper)"/>
          </linearGradient>
        </defs>
        <rect x="0" y="0" width="400" height="140" fill="url(#peakFillCabernet)"/>
      </svg>
      <h1 class="brand-name">CALVENTO</h1>
      <p class="varietal">CABERNET SAUVIGNON</p>
      <p class="vintage">2017</p>
      <p class="origin">VALLE CENTRAL, CHILE</p>
    </article>
  </main>
</body>
</html>
```